Internal Office Slogans / Motto / Vision Statements

Hi. We would like to put up some posters around the office with quotations such as -
-”Do what you do so well that they will want to see it again and bring their friends.”- Harlan Pruett
-Make your customers feel heard and understood. Make your customers feel respected and liked. Make your customers feel appreciated and helped. Understand that you can do none of these things unless you are sincere about them.
Gordon Felsk
- It’s a very predictable and satisfying phenomenon: whenever we get better, our customers do too.
Ray Tolbin
-Catch people in the act of performing extraordinary customer service. Treat them like heroes. Tell their stories, far and wide.
Neil Hartcombe

The purpose of the posters is to reiterate our culture and vision within the organisation. They should be clean, crisp and eye catching, not gaudy or bright. Professional, bold and strong.

The company website and logo is at http://www.norvanta.com.au
Print size will be A1

Thanks for participating & looking forward to seeing your great work.
Updates

Hi All. . 

So to reiterate we are looking for one background design to be used for multiple quotes...  The list of quotes are as follows: 

Support and or Sales Office

 

Make your customers feel heard and understood.Make your customers feel respected and liked. Make your customers feelappreciated and helped. Understand that you can do none of these things unlessyou are sincere about them.

Gordon Felsk

 

Nothing liberates our greatness like the desireto help, the desire to serve

Rosalind Pevrell

 

It’s a very predictable and satisfying phenomenon:whenever we get better, our customers do too.

Ray Tolbin

 

Success means we go to sleep at night knowingthat our talents and abilities were used in a way that served others.

Rosalind Pevrell.

 

The sole purpose of business is to create, serveand satisfy a customer, from beginning to end – and that’s everyone’s job.

Neil Hartcombe

 

We don’t celebrate closing a sale, we celebrateopening a relationship.

Eleanor Quisk

I will never make you a promise – unless I giveyou a plan and procedure to make that promise possible.

Lon Borstad

 

Customers feel we take them for granted; onlyshow interest when we want an order; lavish our time on prospects; communicatemainly by invoice; are fixated on big accounts; drop them like hot potatoesonce we have the order; don’t follow through on promises; and satisfy our ownbureaucracy rather than their needs. We can do better than that, much better.

Peter K Almsby.

 

 

General and public area

 

Catch people in the act of performingextraordinary customer service. Treat them like heroes. Tell their stories, farand wide.

Neil Hartcombe

 

 

We see our customers as invited guests to aparty, and we are the hosts. It’s our job every day to make every importantaspect of the customer experience a little bit better." Carl Dunmore - Founder andCEO of Veltrona

 

"If you do build a great experience,customers tell each other about that. Word of mouth is verypowerful."  Carl Dunmore

 

It's not a faithin technology. It's faith in people. Frank Toller

 

“Being the richest man in the cemetery doesn’tmatter to me … Going to bed at night saying we’ve done something wonderful…that’s what matters to me.” Frank Toller

 

The customer experience is the next competitivebattleground. Terry Mandevic, CIO, Quorra Computers

 

”Do what you do so well that they will want tosee it again and bring their friends.”- Harlan Pruett

In the world of internet customer service, it isimportant to remember your competitor is only a mouse click away. GlennPirsley (not sure who he is but like the quote).

The customer is why you go to work. If they goaway, you do, too. Simon Largotti (?)

 

MaybeSome for Sales or Build Team:

Quality is remembered long after the price is forgotten. Renzoli Family Slogan

```html
<!DOCTYPE html>
<html lang="en">
<head>
<meta charset="utf-8">
<title>Norvanta — Customer Service Poster</title>
<link rel="stylesheet" href="https://fonts.googleapis.com/css2?family=Oswald:wght@500;600&display=swap">
<style>
  :root {
    --page: #ffffff;
    --panel-dark: #000000;
    --panel-light: #474747;
    --quote: #ffffff;
    --accent: #e8141b;
  }
  * { margin: 0; padding: 0; box-sizing: border-box; }
  html, body {
    width: 1200px;
    height: 900px;
    overflow: hidden;
    background: var(--page);
  }
  .poster {
    position: absolute;
    left: 37px;
    top: 52px;
    width: 1121px;
    height: 793px;
    background: linear-gradient(225deg, var(--panel-light) 0%, #1c1c1c 45%, var(--panel-dark) 80%);
  }
  .quote {
    position: absolute;
    left: 0;
    right: 0;
    top: 170px;
    text-align: center;
    font-family: "Oswald", "Arial Narrow", sans-serif;
    font-weight: 500;
    font-size: 55px;
    line-height: 80.5px;
    color: var(--quote);
    letter-spacing: 0.2px;
  }
  .author {
    position: absolute;
    left: 0;
    right: 0;
    top: 585px;
    text-align: center;
    font-family: "Oswald", "Arial Narrow", sans-serif;
    font-weight: 600;
    font-size: 30px;
    line-height: 40px;
    color: var(--accent);
  }
  .brand {
    position: absolute;
    left: 32px;
    top: 742px;
    display: flex;
    align-items: center;
    gap: 5px;
  }
  .brand-mark {
    width: 18px;
    height: 18px;
    background: var(--accent);
  }
  .brand-name {
    font-family: "Oswald", "Arial Narrow", sans-serif;
    font-weight: 600;
    font-size: 19px;
    line-height: 20px;
    color: var(--quote);
  }
</style>
</head>
<body>
  <main class="poster">
    <blockquote class="quote">“Catch people in the act of<br>performing extraordinary<br>customer service. Treat them<br>like heroes. Tell their<br>stories, far and wide.”</blockquote>
    <p class="author">Neil Hartcombe</p>
    <div class="brand">
      <span class="brand-mark"></span>
      <span class="brand-name">Norvanta</span>
    </div>
  </main>
</body>
</html>
```